Luxury Business Card Design

We need a business card design for a law firm that look sophisticated and luxury

Target Market(s)

Australian legal markets

Industry/Entity Type

Legal

Contact Information for Business Card

Attached

Requirements
Must have
• Logo, head office address on front side and 2 other addresses on the back side.
Nice to have
• Please see below our current business card. Need something more sophisticated and luxury feel

```html
<!DOCTYPE html>
<html lang="en">
<head>
<meta charset="utf-8">
<title>Harlow Lawyers – Business Card</title>
<link rel="stylesheet" href="https://fonts.googleapis.com/css2?family=EB+Garamond:wght@400;500;700&display=swap">
<style>
  :root {
    --bg: #d9d9d7;
    --paper: #ffffff;
    --forest: #0b1a12;
    --gold: #b8913e;
    --ink: #111a14;
    --grey: #4a4a4a;
    --rule-gold: rgba(184,145,62,0.55);
  }
  * { box-sizing: border-box; margin: 0; padding: 0; }
  html, body { width: 1200px; height: 900px; overflow: hidden; }
  body {
    background: var(--bg);
    font-family: "EB Garamond", Georgia, serif;
    display: flex; align-items: center; justify-content: center; gap: 60px;
  }
  .card {
    width: 420px; height: 690px;
    display: flex; flex-direction: column; align-items: center;
    text-align: center;
    overflow: hidden;
    box-shadow: 0 10px 30px rgba(0,0,0,0.18);
  }
  .card > * { flex-shrink: 0; }
  .card--front { background: var(--paper); color: var(--grey); padding-top: 92px; }
  .card--back { background: var(--forest); color: #e9e6dd; padding-top: 74px; }

  .brand-mark { display: block; width: 140px; height: 140px; }
  .card--back .brand-mark { width: 100px; height: 100px; }
  .brand-name {
    font-weight: 500; font-size: 22px; letter-spacing: 6px;
    text-transform: uppercase; margin-top: 14px;
  }
  .card--front .brand-name { color: var(--gold); }
  .card--back .brand-name { color: #ffffff; font-size: 32px; letter-spacing: 3px; margin-top: 16px; line-height: 1.1; }

  .person-name { font-weight: 700; font-size: 26px; color: var(--ink); letter-spacing: 1px; margin-top: 30px; }
  .person-role { font-size: 18px; line-height: 1.25; margin-top: 4px; }
  .rule { width: 300px; height: 1px; background: var(--rule-gold); margin: 16px 0; }
  .contact-line { display: flex; align-items: center; justify-content: center; gap: 10px; font-size: 19px; line-height: 1.35; }
  .contact-line svg { width: 16px; height: 16px; flex: none; }
  .address { font-size: 20px; line-height: 1.3; }

  .office { font-size: 16px; line-height: 1.3; }
  .office--first { margin-top: 26px; }
  .office-title { color: var(--gold); text-transform: uppercase; font-size: 16px; letter-spacing: 0.5px; }
  .office-phone span { color: var(--gold); }
  .card--back .rule { width: 320px; margin: 14px auto; }
  .tagline {
    margin-top: auto; margin-bottom: 40px;
    font-weight: 700; font-size: 16px; letter-spacing: 0.5px;
    text-transform: uppercase; color: #ffffff;
  }
</style>
</head>
<body>

  <section class="card card--front">
    <svg class="brand-mark" viewBox="0 0 150 150" aria-hidden="true">
      <circle cx="75" cy="75" r="70" fill="none" stroke="#b8913e" stroke-width="5"/>
    </svg>
    <div class="brand-name">Harlow</div>

    <div class="person-name">DANIEL MERCER</div>
    <div class="person-role">Director and Principal Solicitor<br>MBA, Juris Doctor</div>
    <div class="contact-line" style="margin-top:6px">
      <svg viewBox="0 0 16 16" aria-hidden="true"><rect x="4" y="1" width="8" height="14" rx="1.5" fill="none" stroke="#b8913e" stroke-width="1.4"/></svg>
      +61 7 3000 4120
    </div>

    <div class="rule"></div>
    <div class="address">Level 5/88 Ashby Terrace<br>Kelvin Grove QLD 4059, Australia</div>
    <div class="rule"></div>

    <div class="contact-line">
      <svg viewBox="0 0 16 16" aria-hidden="true"><path d="M3 2l3 0 1 3-2 1.5a9 9 0 0 0 4.5 4.5L11 9l3 1v3a1 1 0 0 1-1 1A12 12 0 0 1 2 3a1 1 0 0 1 1-1z" fill="#b8913e"/></svg>
      +61 0400 123 456
    </div>
    <div class="contact-line">
      <svg viewBox="0 0 16 16" aria-hidden="true"><rect x="1.5" y="3.5" width="13" height="9" fill="none" stroke="#b8913e" stroke-width="1.4"/><path d="M1.5 3.5l6.5 5 6.5-5" fill="none" stroke="#b8913e" stroke-width="1.4"/></svg>
      daniel@harlowlawyers.com.au
    </div>
    <div class="contact-line">
      <svg viewBox="0 0 16 16" aria-hidden="true"><circle cx="8" cy="8" r="6.5" fill="none" stroke="#b8913e" stroke-width="1.3"/><ellipse cx="8" cy="8" rx="3" ry="6.5" fill="none" stroke="#b8913e" stroke-width="1.1"/><path d="M1.5 8h13" stroke="#b8913e" stroke-width="1.1"/></svg>
      www.harlowlawyers.com.au
    </div>
  </section>

  <section class="card card--back">
    <svg class="brand-mark" viewBox="0 0 150 150" aria-hidden="true">
      <circle cx="75" cy="75" r="68" fill="none" stroke="#b8913e" stroke-width="6"/>
    </svg>
    <div class="brand-name">Harlow Lawyers</div>

    <div class="office office--first">
      <div class="office-title">Melbourne Office</div>
      Suite 410, Ashford Chambers<br>
      212 Little Bourke Street, Melbourne, VIC, 3000
      <div class="office-phone"><span>P:</span> (03) 9000 1234</div>
    </div>
    <div class="rule"></div>
    <div class="office">
      <div class="office-title">Sydney</div>
      Level 12, Kingsford Building, 45 Station Street<br>
      PARRAMATTA, NSW 2150
      <div class="office-phone"><span>P:</span> +61 02 8000 4321</div>
    </div>
    <div class="rule"></div>
    <div class="office">
      <div class="office-title">Perth Office</div>
      Unit 4, 17 Lakeside Drive<br>
      Joondalup, WA, 6027
      <div class="office-phone"><span>P:</span> 0400 123 456</div>
    </div>
    <div class="rule"></div>

    <div class="tagline">Clear advice. Firm counsel. Every client</div>
  </section>

</body>
</html>
```